Tallow Inks needs a new Webpage for their collection of ballpens

We at Tallow inks need a brand new webpage to represent our company and range of products. We need a product based website to focus purely on our collection. The web design must bring about a perception of high quality International brand but still affordable in price. Since there are only 5 products, they must all feature on the cover page itself.

Target Market(s)

Stationary Wholesale and retail

Industry/Entity Type

It Company

Number of Pages Required

1 page

Requirements
Must have
• pls see www.quambrite.example to derive inspiration
Should not have
• stock images
• abstract images
• random pen images

```html
<!DOCTYPE html>
<html lang="en">
<head>
<meta charset="utf-8">
<title>Tallow Inks — Ballpens</title>
<link href="https://fonts.googleapis.com/css2?family=Archivo:wght@400;500;600;700&family=Lato:wght@400;700&display=swap" rel="stylesheet">
<style>
  :root {
    --brand-blue: #1a63a6;
    --ink: #161616;
    --band-grey: #6a7076;
    --spec-bg: #f2f2f2;
    --card-line: #e3e3e3;
    --footer: #1b1c1e;
    --pen-violet: #3d2a9a;
    --pen-sky: #7fc0e8;
    --swatch-red: #e2461e;
    --white: #ffffff;
  }
  * { box-sizing: border-box; margin: 0; padding: 0; }
  html, body { width: 755px; height: 1200px; overflow: hidden; background: var(--white); }
  body { position: relative; font-family: "Archivo", Arial, sans-serif; color: var(--ink); }

  .site-header { position: absolute; top: 0; left: 0; width: 755px; height: 80px; z-index: 2; }
  .brand-name { position: absolute; left: 50px; top: 29px; font-size: 17px; font-weight: 700; letter-spacing: 2px; color: var(--brand-blue); }
  .main-nav { position: absolute; right: 50px; top: 32px; display: flex; gap: 15px; }
  .main-nav a { font-size: 8.5px; font-weight: 600; color: var(--ink); text-decoration: none; }

  .hero { position: absolute; top: 0; left: 0; width: 755px; height: 448px; }
  .hero-pens { position: absolute; right: 0; top: 0; width: 400px; height: 310px;
    background: linear-gradient(200deg, rgba(61,42,154,0.55) 0%, rgba(127,192,232,0.45) 45%, rgba(255,255,255,0) 80%);
    clip-path: polygon(0 0, 100% 0, 100% 100%, 85% 100%); }
  .hero-title { position: absolute; top: 240px; left: 0; width: 710px; text-align: center; font-size: 16px; font-weight: 600; letter-spacing: 0.8px; line-height: 22px; }
  .hero-pen { position: absolute; left: 176px; top: 295px; width: 348px; height: 20px; border-radius: 10px;
    background: linear-gradient(90deg, var(--pen-violet) 0%, #e8e8ee 8%, #f4f4f6 70%, var(--pen-violet) 72%, var(--pen-violet) 100%); }

  .info-band { position: absolute; top: 448px; left: 0; width: 755px; height: 255px; background: var(--band-grey); color: var(--white); }
  .info-band h2 { font-size: 16px; font-weight: 600; letter-spacing: 0.5px; }
  .about { position: absolute; left: 51px; top: 36px; width: 306px; }
  .about p { font-size: 7.1px; font-weight: 500; line-height: 13.4px; margin-top: 14px; }
  .about p + p { margin-top: 9px; }
  .features { position: absolute; left: 396px; top: 36px; width: 310px; }
  .feature-diagram { width: 306px; height: 74px; margin-top: 20px; border-radius: 4px;
    background: linear-gradient(180deg, rgba(255,255,255,0.55) 0%, rgba(255,255,255,0.25) 100%); }
  .features p { font-size: 7.1px; font-weight: 500; line-height: 13.4px; margin-top: 34px; }

  .products { position: absolute; top: 703px; left: 0; width: 755px; }
  .products h2 { text-align: center; font-size: 16px; font-weight: 600; margin-top: 30px; letter-spacing: 0.5px; }
  .product-card { position: absolute; top: 95px; width: 113px; height: 339px; border: 1px solid var(--card-line); background: var(--white); }
  .product-photo { position: absolute; left: 50px; top: 22px; width: 12px; height: 178px; border-radius: 5px;
    background: linear-gradient(180deg, var(--pen-violet) 0%, #f2f2f6 25%, #e6e6ec 85%, var(--pen-violet) 100%); }
  .product-photo.sky { background: linear-gradient(180deg, #9bcdec 0%, var(--pen-sky) 80%, #4b9fd6 100%); }
  .product-name { position: absolute; top: 216px; width: 100%; text-align: center; font-size: 7.2px; font-weight: 600; }
  .spec-table { position: absolute; top: 235px; left: 0; width: 100%; height: 60px; background: var(--spec-bg); padding: 5px 8px 0; font-family: "Lato", Arial, sans-serif; font-size: 6.8px; }
  .spec-row { height: 17px; line-height: 17px; border-bottom: 1px solid #e2e2e2; }
  .spec-row:last-child { border-bottom: 0; display: flex; align-items: center; gap: 3px; }
  .spec-label { color: var(--brand-blue); }
  .swatch { display: inline-block; width: 9px; height: 9px; }
  .swatch.blue { background: var(--brand-blue); margin-left: 6px; }
  .swatch.black { background: var(--ink); }
  .swatch.red { background: var(--swatch-red); }
  .buy-button { position: absolute; top: 309px; left: 33px; width: 44px; height: 16px; background: var(--brand-blue); color: var(--white);
    font-size: 6.4px; font-weight: 600; text-align: center; line-height: 16px; text-decoration: none; }

  .site-footer { position: absolute; top: 1154px; left: 0; width: 755px; height: 46px; background: var(--footer); }
  .copyright { position: absolute; left: 51px; top: 16px; font-size: 6.6px; color: var(--white); }
  .footer-brand { position: absolute; right: 50px; top: 11px; font-size: 17px; font-weight: 700; letter-spacing: 2px; color: var(--brand-blue); }
</style>
</head>
<body>
  <section class="hero">
    <div class="hero-pens" role="img" aria-label="Cascade of violet and sky-blue ballpens falling diagonally"></div>
    <h1 class="hero-title">WRITING WILL NOT BE OVER<br>WITH TALLOW</h1>
    <div class="hero-pen" role="img" aria-label="Tallow Nova ballpen lying horizontally with soft shadow"></div>
  </section>

  <header class="site-header">
    <div class="brand-name">TALLOW INKS</div>
    <nav class="main-nav">
      <a href="#">HOME</a><a href="#">ABOUT US</a><a href="#">LUMINA</a><a href="#">VELA</a>
      <a href="#">ARKO</a><a href="#">ZEPHY</a><a href="#">NOVA</a><a href="#">CONTACT US</a>
    </nav>
  </header>

  <section class="info-band">
    <div class="about">
      <h2>ABOUT US</h2>
      <p>Lorem ipsum dolor sit amet, consectetur adipiscing elit. Cras efficitur justo eu laoreet volutpat. Duis dignissim nibh vitae magna fringilla sagittis. Praesent felis odio, blandit pharetra tempus eget, posuere eu tellus. Mauris at nulla eget velit ultricies tincidunt id nec quam. Quisque dui libero, ultrices in diam et, imperdiet hendrerit enim. Morbi ante felis, imperdiet ut porta et, dictum ultricies velit. Fusce a elit et lacus viverra volutpat. Nulla dictum metus vitae laoreet accumsan. Aliquam maximus erat vel malesuada hendrerit. Vestibulum gravida tempus nunc eget molestie.</p>
      <p>Proin nisl nisl, porta bibendum ante id, commodo tempor orci. Phasellus sed tellus in tortor convallis faucibus et sagittis odio. Sed ante turpis, iaculis et ex ut, lacinia iaculis quam.</p>
    </div>
    <div class="features">
      <h2>FEATURES</h2>
      <div class="feature-diagram" role="img" aria-label="Feature diagram of three white ribbon waves with four numbered markers"></div>
      <p>Nulla pretium sed mauris non viverra. Integer vitae vehicula nulla. Fusce ac massa non velit maximus fermentum ac at augue. Mauris nunc orci, vestibulum eu lobortis in, eleifend ut est.</p>
    </div>
  </section>

  <section class="products">
    <h2>PRODUCTS</h2>

    <article class="product-card" style="left:51px">
      <div class="product-photo" role="img" aria-label="Tallow Lumina ballpen, violet cap and clear barrel"></div>
      <h3 class="product-name">TALLOW LUMINA</h3>
      <div class="spec-table">
        <div class="spec-row"><span class="spec-label">Tip Size:</span> 0.7 mm</div>
        <div class="spec-row"><span class="spec-label">Pouch:</span> 5 Pieces</div>
        <div class="spec-row"><span class="spec-label">Availlable in:</span><span class="swatch blue"></span><span class="swatch black"></span><span class="swatch red"></span></div>
      </div>
      <a class="buy-button" href="#">Buy Now</a>
    </article>

    <article class="product-card" style="left:186px">
      <div class="product-photo" role="img" aria-label="Tallow Vela ballpen, violet cap and clear barrel"></div>
      <h3 class="product-name">TALLOW VELA</h3>
      <div class="spec-table">
        <div class="spec-row"><span class="spec-label">Tip Size:</span> 0.7 mm</div>
        <div class="spec-row"><span class="spec-label">Pouch:</span> 5 Pieces</div>
        <div class="spec-row"><span class="spec-label">Availlable in:</span><span class="swatch blue"></span><span class="swatch black"></span><span class="swatch red"></span></div>
      </div>
      <a class="buy-button" href="#">Buy Now</a>
    </article>

    <article class="product-card" style="left:321px">
      <div class="product-photo sky" role="img" aria-label="Tallow Zephy ballpen, sky-blue body"></div>
      <h3 class="product-name">TALLOW ZEPHY</h3>
      <div class="spec-table">
        <div class="spec-row"><span class="spec-label">Tip Size:</span> 0.7 mm</div>
        <div class="spec-row"><span class="spec-label">Pouch:</span> 5 Pieces</div>
        <div class="spec-row"><span class="spec-label">Availlable in:</span><span class="swatch blue"></span><span class="swatch black"></span></div>
      </div>
      <a class="buy-button" href="#">Buy Now</a>
    </article>

    <article class="product-card" style="left:457px">
      <div class="product-photo" role="img" aria-label="Tallow Arko ballpen, violet cap and clear barrel"></div>
      <h3 class="product-name">TALLOW ARKO</h3>
      <div class="spec-table">
        <div class="spec-row"><span class="spec-label">Tip Size:</span> 0.7 mm</div>
        <div class="spec-row"><span class="spec-label">Pouch:</span> 5 Pieces</div>
        <div class="spec-row"><span class="spec-label">Availlable in:</span><span class="swatch blue"></span><span class="swatch black"></span></div>
      </div>
      <a class="buy-button" href="#">Buy Now</a>
    </article>

    <article class="product-card" style="left:592px">
      <div class="product-photo" role="img" aria-label="Tallow Nova ballpen, violet cap and clear barrel"></div>
      <h3 class="product-name">TALLOW NOVA</h3>
      <div class="spec-table">
        <div class="spec-row"><span class="spec-label">Tip Size:</span> 0.7 mm</div>
        <div class="spec-row"><span class="spec-label">Box:</span> 5 Pieces</div>
        <div class="spec-row"><span class="spec-label">Availlable in:</span><span class="swatch blue"></span><span class="swatch black"></span></div>
      </div>
      <a class="buy-button" href="#">Buy Now</a>
    </article>
  </section>

  <footer class="site-footer">
    <p class="copyright">© 2015 tallowinks.example. All rights reserved</p>
    <div class="footer-brand">TALLOW INKS</div>
  </footer>
</body>
</html>
```